Beer Sommelier Business Card

Dear Designers,
I'm looking forward a Beer Sommelier business card. I'm a Beer Sommelier and also a Chef in Rio de Janeiro, Brazil but this card has to be a Beer Sommelier card.
I do consulting, brigade training, tastings and harmonizations.
Forget about themes such as rock and roll, motorcycles, conventional English pubs and bellied beer drinkers. This business card will be delivered to restaurant owners and investors in Rio.
It has to seek elegance rather than luxury, and refinement rather than fashion.
I work using a black dress shirt, a Varnel Osterby watch and a 18k 1981 Dumelle aviator eyeglasses. I'm a business man and It's all part of the game.
Obviously, it has to be written in PORTUGUESE (only) and just as little as possible.

Informations to be included:

Tiago Varquim

Beer Sommelier
Chef de Cuisine

Consultoria
Treinamento de Brigada
Degustações
Harmonizações

telephone number (just numbers): 947261380

email (just the adress): tiagovarquim@mailnest.example

PS:
The letter "c" on both words "Degustações" and "Harmonizações" they have a small trace under it.
The letter "o" on both words "Degustações" and "Harmonizações" they have a small wave above it.

Blame the Latin.

Best Regards

Target Market(s)

Restaurant Owners and Investors. I have to impress them with my business card before I offer my services.

Industry/Entity Type

Restaurant

Contact Information for Business Card

An unique and well constructed Sommelier Business Card

Requirements
Must have
• A firts look impact. An unique and well made design. Not an ordinary product.
• Tiago Varquim
• Beer Sommelier/Chef de Cuisine
• Consultoria
• Treinamento de Brigada
• Degustações
• Harmonizações
• telephone number (just numbers): 947261380
• email (just the adress): tiagovarquim@mailnest.example
• PS:
• The letter "c" on both words "Degustações" and "Harmonizações" they have a small trace under it.
• The letter "o" on both words "Degustações" and "Harmonizações" they have a small wave above it.
Nice to have
• Elegance, Refinement.
• Should be a Pro Style good Looking card,
• Forget themes like beer, chef and cuisine,
• It could be a laser engraved, metal, stainless steel, PVC, Triplex, Smooth, Letterpress, all black or any other good idea.
Should not have
• Words like telephone, email, cartoon pics or glass pics.
• Should not be an ordinary card that I could download from the web or use a web program and easily make by my self.
• Just Portuguese words

```html
<!DOCTYPE html>
<html lang="pt">
<head>
<meta charset="utf-8">
<title>Tiago Varquim — Beer Sommelier</title>
<link rel="stylesheet" href="https://fonts.googleapis.com/css2?family=Open+Sans:wght@300;400&display=swap">
<style>
  :root {
    --page-bg: #e8e6e3;
    --card-red: #c23b2d;
    --band-red: #b93428;
    --seal-red: #a32e24;
    --card-white: #f4f2f0;
    --seal-grey: #e2e0de;
    --rule-light: rgba(255,255,255,0.55);
    --ink-red: #b8342a;
  }
  * { box-sizing: border-box; margin: 0; padding: 0; }
  html, body { width: 1200px; height: 873px; overflow: hidden; }
  body {
    background: var(--page-bg);
    font-family: "Open Sans", Arial, sans-serif;
    font-weight: 300;
    position: relative;
  }
  .card {
    position: absolute;
    top: 262px;
    width: 540px;
    height: 348px;
    border-radius: 3px;
    box-shadow: 0 6px 18px rgba(0,0,0,0.14);
    overflow: hidden;
  }

  /* Front face */
  .card--front { left: 45px; background: var(--card-white); }
  .card--front .frame {
    position: absolute; inset: 14px;
    border: 2px solid var(--card-red);
  }
  .identity {
    position: absolute; left: 16px; right: 16px; top: 16px; height: 190px;
    display: flex; align-items: center; justify-content: center; gap: 26px;
  }
  .seal-small {
    width: 92px; height: 92px; border-radius: 50%;
    background: var(--seal-red);
    box-shadow: inset 0 0 0 4px var(--seal-red), inset 0 0 0 6px rgba(255,255,255,0.85);
    display: flex; align-items: center; justify-content: center; text-align: center;
    color: #f3e3df; font-size: 11px; line-height: 1.25; letter-spacing: 1px; text-transform: uppercase;
  }
  .role { color: var(--ink-red); }
  .role__title { font-size: 27px; letter-spacing: 1.5px; font-weight: 400; }
  .role__sub { font-size: 18px; margin-top: 2px; padding-left: 10px; }

  .contact-band {
    position: absolute; left: 16px; right: 16px; bottom: 16px; height: 126px;
    background: var(--band-red);
    display: grid; grid-template-columns: 1.15fr 0.9fr 1.35fr;
  }
  .contact-cell {
    position: relative;
    display: flex; flex-direction: column; align-items: center; justify-content: flex-start;
    padding-top: 14px; gap: 9px;
    color: #f6e6e2; font-size: 12px; text-align: center; line-height: 1.35;
  }
  .contact-cell + .contact-cell { border-left: 1px solid var(--rule-light); }
  .contact-cell .icon {
    width: 24px; height: 24px; border-radius: 50%;
    background: #f6e6e2; display: flex; align-items: center; justify-content: center;
    flex: none;
  }
  .contact-cell .phone-number { font-size: 16px; letter-spacing: 1px; margin-top: 10px; }
  .contact-cell .email { font-size: 11.5px; margin-top: 12px; }

  /* Back face */
  .card--back { left: 615px; background: var(--card-red); }
  .card--back .frame {
    position: absolute; inset: 14px;
    border: 1.5px solid rgba(255,255,255,0.9);
  }
  .seal-large {
    position: absolute; left: 50%; top: 50%;
    width: 196px; height: 196px; margin: -98px 0 0 -98px;
    border-radius: 50%;
    border: 3px solid #f6f1ef;
    display: flex; align-items: center; justify-content: center;
  }
  .seal-large__face {
    width: 166px; height: 166px; border-radius: 50%;
    background: var(--seal-grey);
    display: flex; align-items: center; justify-content: center; text-align: center;
    color: var(--ink-red); font-size: 22px; line-height: 1.15; letter-spacing: 2px;
    text-transform: uppercase;
  }
</style>
</head>
<body>

  <section class="card card--front" aria-label="Frente do cartão">
    <div class="frame"></div>
    <div class="identity">
      <div class="seal-small">Tiago<br>Varquim</div>
      <div class="role">
        <p class="role__title">BEER SOMMELIER</p>
        <p class="role__sub">(Chef de Cuisine)</p>
      </div>
    </div>
    <div class="contact-band">
      <div class="contact-cell">
        <span class="icon">
          <svg width="12" height="14" viewBox="0 0 12 14"><path d="M6 1a4 4 0 0 0-4 4c0 3 4 8 4 8s4-5 4-8a4 4 0 0 0-4-4z" fill="#b93428"/><circle cx="6" cy="5" r="1.5" fill="#f6e6e2"/></svg>
        </span>
        <p>Consultoria<br>Treinamento de Brigada<br>Degustações<br>Harmonizações</p>
      </div>
      <div class="contact-cell">
        <span class="icon">
          <svg width="12" height="12" viewBox="0 0 12 12"><path d="M3 1l2 2.5-1.2 1.3c.6 1.3 1.6 2.3 2.9 2.9L8 6.5 10.5 8.5 9.5 10.5C5.5 10.5 1.5 6.5 1.5 2.5z" fill="#b93428"/></svg>
        </span>
        <p class="phone-number">947261380</p>
      </div>
      <div class="contact-cell">
        <span class="icon">
          <svg width="13" height="13" viewBox="0 0 13 13"><circle cx="6.5" cy="6.5" r="2" fill="none" stroke="#b93428" stroke-width="1.4"/><path d="M8.5 6.5v1a1.5 1.5 0 0 0 3 0v-1a5 5 0 1 0-2 4" fill="none" stroke="#b93428" stroke-width="1.4"/></svg>
        </span>
        <p class="email">tiagovarquim@mailnest.example</p>
      </div>
    </div>
  </section>

  <section class="card card--back" aria-label="Verso do cartão">
    <div class="frame"></div>
    <div class="seal-large">
      <div class="seal-large__face">Tiago<br>Varquim</div>
    </div>
  </section>

</body>
</html>
```